Verdant Loop Advisors, LLC

I am looking for a simple, clear layout with my logo prominent and embossed, on the best quality card stock available. I would like the business name and phone number included on the card as well......I dont want my name anywhere on the card and I would like my logo embossed on the card......something simple with a white back......open to designs as long as they go along with recycling symbols and green type stuff.....The address, website, cell number, fax number, and email are listed below

5374 Tillbury Fenwood Road
Hyattsville, MD 20785

c. 240.555.0143 f. 240.555.0187
e. sales@verdantloopadvisors.example
w. www.verdantloopadvisors.example

Industry/Entity Type

Recycling

```html
<!DOCTYPE html>
<html lang="en">
<head>
<meta charset="utf-8">
<title>Verdant Loop Advisors, LLC — Business Card</title>
<link rel="stylesheet" href="https://fonts.googleapis.com/css2?family=Michroma&display=swap">
<style>
  :root {
    --page-bg: #e9e7e3;
    --card-white: #fbfbfb;
    --card-shade: #ececec;
    --ink-dark: #2d2826;
    --ink-grey: #4a4a4a;
    --leaf-green: #1f6b3b;
    --divider: #bdbdbd;
  }
  * { margin: 0; padding: 0; box-sizing: border-box; }
  html, body {
    width: 1200px; height: 900px; overflow: hidden;
    background: var(--page-bg);
    font-family: "Michroma", sans-serif;
  }
  .business-card {
    position: absolute; left: 150px; top: 193px;
    width: 900px; height: 514px;
    border-radius: 34px; overflow: hidden;
    background: linear-gradient(160deg, var(--card-white) 40%, var(--card-shade) 100%);
    box-shadow: 0 14px 34px rgba(0,0,0,0.18);
  }
  .edge-swoosh { position: absolute; inset: 0; width: 900px; height: 514px; }
  .brand {
    position: absolute; left: 300px; top: 100px;
    display: flex; align-items: center; gap: 18px;
  }
  .brand-dot {
    width: 54px; height: 54px; border-radius: 50%;
    background: var(--leaf-green); flex: none;
  }
  .brand-name {
    font-size: 27px; line-height: 1.25; letter-spacing: 1px;
    color: var(--ink-dark); text-transform: uppercase;
  }
  .contact-block {
    position: absolute; left: 215px; top: 248px;
    display: flex; align-items: stretch;
  }
  .identity {
    width: 325px; padding-right: 22px; text-align: right;
    display: flex; flex-direction: column; justify-content: flex-end;
  }
  .address {
    font-size: 13px; color: var(--ink-grey); line-height: 1.6;
    font-variant: small-caps; white-space: nowrap;
  }
  .divider { width: 1px; background: var(--divider); }
  .reach { padding-left: 20px; font-size: 14px; color: var(--ink-grey); }
  .reach-group + .reach-group { margin-top: 16px; }
  .reach-line { display: flex; align-items: center; gap: 9px; height: 24px; letter-spacing: 0.5px; white-space: nowrap; }
  .reach-line.lowercase { font-variant: small-caps; font-size: 13px; }
  .reach-icon { width: 16px; height: 16px; flex: none; }
</style>
</head>
<body>
  <div class="business-card">
    <svg class="edge-swoosh" viewBox="0 0 900 514" aria-hidden="true">
      <path d="M0,40 C40,270 150,430 262,514 L0,514 Z" fill="var(--ink-dark)"/>
      <path d="M14,40 C62,280 180,440 300,514" fill="none" stroke="var(--leaf-green)" stroke-width="8"/>
    </svg>

    <div class="brand">
      <span class="brand-dot"></span>
      <span class="brand-name">Verdant Loop<br>Advisors, LLC</span>
    </div>

    <div class="contact-block">
      <div class="identity">
        <p class="address">5374 Tillbury Fenwood Road,<br>Hyattsville, MD 20785</p>
      </div>
      <div class="divider"></div>
      <div class="reach">
        <div class="reach-group">
          <p class="reach-line">
            <svg class="reach-icon" viewBox="0 0 16 16" aria-hidden="true"><circle cx="8" cy="8" r="8" fill="var(--ink-dark)"/><path d="M5,4 L7,4 L7.5,6 L6.5,7 Q7.5,9 9,9.5 L10,8.5 L12,9 L12,11 Q7,12 4,6 Z" fill="#fff"/></svg>
            c. 240.555.0143
          </p>
          <p class="reach-line">
            <svg class="reach-icon" viewBox="0 0 16 16" aria-hidden="true"><circle cx="8" cy="8" r="8" fill="var(--ink-dark)"/><rect x="5.5" y="3.5" width="5" height="9" rx="1" fill="#fff"/></svg>
            f. 240.555.0187
          </p>
          <p class="reach-line">
            <svg class="reach-icon" viewBox="0 0 16 16" aria-hidden="true"><circle cx="8" cy="8" r="8" fill="var(--ink-dark)"/><rect x="4" y="6" width="8" height="5" fill="#fff"/><rect x="5.5" y="3.5" width="5" height="3" fill="#fff"/></svg>
            240.555.0162
          </p>
        </div>
        <div class="reach-group">
          <p class="reach-line lowercase">
            <svg class="reach-icon" viewBox="0 0 16 16" aria-hidden="true"><circle cx="8" cy="8" r="8" fill="var(--ink-dark)"/><rect x="4" y="5" width="8" height="6" fill="#fff"/><path d="M4,5 L8,8.5 L12,5" fill="none" stroke="var(--ink-dark)" stroke-width="1"/></svg>
            sales@verdantloopadvisors.example
          </p>
          <p class="reach-line lowercase">
            <svg class="reach-icon" viewBox="0 0 16 16" aria-hidden="true"><circle cx="8" cy="8" r="8" fill="var(--ink-dark)"/><circle cx="8" cy="8" r="4.5" fill="none" stroke="#fff" stroke-width="1"/><path d="M3.5,8 H12.5 M8,3.5 V12.5" stroke="#fff" stroke-width="1"/></svg>
            www.verdantloopadvisors.example
          </p>
        </div>
      </div>
    </div>
  </div>
</body>
</html>
```